MTSS Pyramid graphic needed for use in presentations and on my website

I am a consultant and need graphics to represent the MTSS pyramid (educational terminology) for use on my website and in slide decks. I've included documentation below that shows the MTSS pyramid, some preferences I have thought of, and my color palette. The MTSS pyramid is well-known in my field and I'd like one that I can use in all my presentations and on my website that looks professional and modern.

Target Market(s)

Educational leaders and educators

Industry/Entity Type

Educational Consulting

Font styles to use
Serif
Sans Serif

Colors
00AB8E
00BBA5
67D7C9
C6EFE9
E9F9F6
6B429C
8869AF
B7A5CE
E3DAEB
F3F0F8

Requirements
Must have
• a pyramid that can be recognized as an MTSS pyramid, use of colors that align with my color palette, a professional, modern look and feel, 3 sections with the largest at the bottom of the pyramid
Nice to have
• rounded corners, maybe 3D
Should not have
• a pyramid in a different shape or orientation, any more or fewer than 3 sections

```html
<!DOCTYPE html>
<html lang="en">
<head>
<meta charset="utf-8">
<title>MTSS Pyramid Variations</title>
<link rel="stylesheet" href="https://fonts.googleapis.com/css2?family=Montserrat:wght@400;500;600;700&display=swap">
<style>
  :root {
    --page: #ffffff;
    --slate-hi: #6b7596;
    --slate-lo: #2c3145;
    --lavender-hi: #c3c8e4;
    --lavender-lo: #6f78ab;
    --steel-hi: #5a9bb2;
    --steel-lo: #1f4762;
    --cyan-hi: #bdeef2;
    --cyan-lo: #2fb1c4;
    --teal-hi: #86cfc1;
    --teal-lo: #2a8673;
    --mint-hi: #def7f4;
    --mint-lo: #6fd1c6;
    --label-light: #ffffff;
    --label-dark: #111418;
  }
  html, body {
    margin: 0;
    padding: 0;
    width: 1200px;
    height: 3333px;
    overflow: hidden;
    background: var(--page);
  }
  .canvas {
    position: relative;
    width: 1200px;
    height: 3333px;
  }
  .defs { position: absolute; width: 0; height: 0; }
  .pyramid {
    position: absolute;
    width: 431px;
    height: 380px;
    overflow: visible;
  }
  .col-plain { left: 120px; }
  .col-labelled { left: 636px; }
  .row-1 { top: 297px; }
  .row-2 { top: 878px; }
  .row-3 { top: 1458px; }
  .row-4 { top: 2039px; }
  .row-5 { top: 2620px; }

  .s-slate-hi { stop-color: var(--slate-hi); }
  .s-slate-lo { stop-color: var(--slate-lo); }
  .s-lav-hi { stop-color: var(--lavender-hi); }
  .s-lav-lo { stop-color: var(--lavender-lo); }
  .s-steel-hi { stop-color: var(--steel-hi); }
  .s-steel-lo { stop-color: var(--steel-lo); }
  .s-cyan-hi { stop-color: var(--cyan-hi); }
  .s-cyan-lo { stop-color: var(--cyan-lo); }
  .s-teal-hi { stop-color: var(--teal-hi); }
  .s-teal-lo { stop-color: var(--teal-lo); }
  .s-mint-hi { stop-color: var(--mint-hi); }
  .s-mint-lo { stop-color: var(--mint-lo); }

  .seam { stroke: rgba(0,0,0,0.35); stroke-width: 1.5; }
  .gloss { fill: rgba(255,255,255,0.12); }

  .label {
    font-family: "Montserrat", sans-serif;
    text-anchor: middle;
  }
  .tier-no { font-size: 16px; font-weight: 400; }
  .tier-3-name { font-size: 17px; font-weight: 600; }
  .tier-2-name { font-size: 25px; font-weight: 600; }
  .tier-1-name { font-size: 29px; font-weight: 600; letter-spacing: 0.3px; }
  .on-dark { fill: var(--label-light); }
  .on-dark.tier-no { opacity: 0.75; }
  .on-light { fill: var(--label-dark); }
  .on-dark.tier-2-name, .on-dark.tier-1-name { filter: drop-shadow(0 1px 2px rgba(0,0,0,0.45)); }
  .on-light.tier-2-name, .on-light.tier-1-name { filter: drop-shadow(0 1px 2px rgba(255,255,255,0.7)); }
</style>
</head>
<body>
<div class="canvas">

  <svg class="defs" aria-hidden="true">
    <defs>
      <clipPath id="pyramid-shape">
        <path d="M187 22 Q215.5 -22 244 22 L424 338 Q446 382 398 380 Q215.5 392 33 380 Q-15 382 7 338 Z"/>
      </clipPath>
      <linearGradient id="top-slate" x1="0" y1="0" x2="0" y2="1">
        <stop offset="0" class="s-slate-hi"/><stop offset="1" class="s-slate-lo"/>
      </linearGradient>
      <linearGradient id="top-lavender" x1="0" y1="0" x2="0" y2="1">
        <stop offset="0" class="s-lav-hi"/><stop offset="1" class="s-lav-lo"/>
      </linearGradient>
      <linearGradient id="mid-steel" x1="0" y1="0" x2="0" y2="1">
        <stop offset="0" class="s-steel-hi"/><stop offset="1" class="s-steel-lo"/>
      </linearGradient>
      <linearGradient id="mid-cyan" x1="0" y1="0" x2="0" y2="1">
        <stop offset="0" class="s-cyan-hi"/><stop offset="1" class="s-cyan-lo"/>
      </linearGradient>
      <linearGradient id="base-teal" x1="0" y1="0" x2="0" y2="1">
        <stop offset="0" class="s-teal-hi"/><stop offset="1" class="s-teal-lo"/>
      </linearGradient>
      <linearGradient id="base-mint" x1="0" y1="0" x2="0" y2="1">
        <stop offset="0" class="s-mint-hi"/><stop offset="1" class="s-mint-lo"/>
      </linearGradient>
    </defs>
  </svg>

  <!-- Row 1: slate / steel / teal -->
  <svg class="pyramid col-plain row-1" viewBox="0 0 431 380" role="img" aria-label="Three-tier MTSS pyramid">
    <g clip-path="url(#pyramid-shape)">
      <rect y="-10" width="431" height="137" fill="url(#top-slate)"/>
      <rect y="127" width="431" height="127" fill="url(#mid-steel)"/>
      <rect y="254" width="431" height="140" fill="url(#base-teal)"/>
      <line class="seam" x1="0" y1="127" x2="431" y2="127"/>
      <line class="seam" x1="0" y1="254" x2="431" y2="254"/>
    </g>
  </svg>
  <svg class="pyramid col-labelled row-1" viewBox="0 0 431 380" role="img" aria-label="MTSS pyramid with tier labels">
    <g clip-path="url(#pyramid-shape)">
      <rect y="-10" width="431" height="137" fill="url(#top-slate)"/>
      <rect y="127" width="431" height="127" fill="url(#mid-steel)"/>
      <rect y="254" width="431" height="140" fill="url(#base-teal)"/>
      <line class="seam" x1="0" y1="127" x2="431" y2="127"/>
      <line class="seam" x1="0" y1="254" x2="431" y2="254"/>
    </g>
    <text class="label tier-no on-dark" x="215.5" y="36">Tier 3</text>
    <text class="label tier-3-name on-dark" x="215.5" y="75">Intensive</text>
    <text class="label tier-3-name on-dark" x="215.5" y="95">Intervention</text>
    <text class="label tier-no on-dark" x="215.5" y="162">Tier 2</text>
    <text class="label tier-2-name on-dark" x="215.5" y="198">Targeted</text>
    <text class="label tier-2-name on-dark" x="215.5" y="226">Intervention</text>
    <text class="label tier-no on-dark" x="215.5" y="291">Tier 1</text>
    <text class="label tier-1-name on-dark" x="215.5" y="331">Core Instruction</text>
  </svg>

  <!-- Row 2: slate / steel / mint -->
  <svg class="pyramid col-plain row-2" viewBox="0 0 431 380" role="img" aria-label="Three-tier MTSS pyramid">
    <g clip-path="url(#pyramid-shape)">
      <rect y="-10" width="431" height="137" fill="url(#top-slate)"/>
      <rect y="127" width="431" height="127" fill="url(#mid-steel)"/>
      <rect y="254" width="431" height="140" fill="url(#base-mint)"/>
      <line class="seam" x1="0" y1="127" x2="431" y2="127"/>
      <line class="seam" x1="0" y1="254" x2="431" y2="254"/>
    </g>
  </svg>
  <svg class="pyramid col-labelled row-2" viewBox="0 0 431 380" role="img" aria-label="MTSS pyramid with tier labels">
    <g clip-path="url(#pyramid-shape)">
      <rect y="-10" width="431" height="137" fill="url(#top-slate)"/>
      <rect y="127" width="431" height="127" fill="url(#mid-steel)"/>
      <rect y="254" width="431" height="140" fill="url(#base-mint)"/>
      <line class="seam" x1="0" y1="127" x2="431" y2="127"/>
      <line class="seam" x1="0" y1="254" x2="431" y2="254"/>
    </g>
    <text class="label tier-no on-dark" x="215.5" y="36">Tier 3</text>
    <text class="label tier-3-name on-dark" x="215.5" y="75">Intensive</text>
    <text class="label tier-3-name on-dark" x="215.5" y="95">Intervention</text>
    <text class="label tier-no on-dark" x="215.5" y="162">Tier 2</text>
    <text class="label tier-2-name on-dark" x="215.5" y="198">Targeted</text>
    <text class="label tier-2-name on-dark" x="215.5" y="226">Intervention</text>
    <text class="label tier-no on-light" x="215.5" y="291">Tier 1</text>
    <text class="label tier-1-name on-light" x="215.5" y="331">Core Instruction</text>
  </svg>

  <!-- Row 3: slate / cyan / teal -->
  <svg class="pyramid col-plain row-3" viewBox="0 0 431 380" role="img" aria-label="Three-tier MTSS pyramid">
    <g clip-path="url(#pyramid-shape)">
      <rect y="-10" width="431" height="137" fill="url(#top-slate)"/>
      <rect y="127" width="431" height="127" fill="url(#mid-cyan)"/>
      <rect y="254" width="431" height="140" fill="url(#base-teal)"/>
      <line class="seam" x1="0" y1="127" x2="431" y2="127"/>
      <line class="seam" x1="0" y1="254" x2="431" y2="254"/>
    </g>
  </svg>
  <svg class="pyramid col-labelled row-3" viewBox="0 0 431 380" role="img" aria-label="MTSS pyramid with tier labels">
    <g clip-path="url(#pyramid-shape)">
      <rect y="-10" width="431" height="137" fill="url(#top-slate)"/>
      <rect y="127" width="431" height="127" fill="url(#mid-cyan)"/>
      <rect y="254" width="431" height="140" fill="url(#base-teal)"/>
      <line class="seam" x1="0" y1="127" x2="431" y2="127"/>
      <line class="seam" x1="0" y1="254" x2="431" y2="254"/>
    </g>
    <text class="label tier-3-name on-dark" x="215.5" y="75">Intensive</text>
    <text class="label tier-3-name on-dark" x="215.5" y="95">Intervention</text>
    <text class="label tier-no on-light" x="215.5" y="162">Tier 2</text>
    <text class="label tier-2-name on-light" x="215.5" y="198">Targeted</text>
    <text class="label tier-2-name on-light" x="215.5" y="226">Intervention</text>
    <text class="label tier-no on-dark" x="215.5" y="291">Tier 1</text>
    <text class="label tier-1-name on-dark" x="215.5" y="331">Core Instruction</text>
  </svg>

  <!-- Row 4: lavender / steel / teal -->
  <svg class="pyramid col-plain row-4" viewBox="0 0 431 380" role="img" aria-label="Three-tier MTSS pyramid">
    <g clip-path="url(#pyramid-shape)">
      <rect y="-10" width="431" height="137" fill="url(#top-lavender)"/>
      <rect y="127" width="431" height="127" fill="url(#mid-steel)"/>
      <rect y="254" width="431" height="140" fill="url(#base-teal)"/>
      <line class="seam" x1="0" y1="127" x2="431" y2="127"/>
      <line class="seam" x1="0" y1="254" x2="431" y2="254"/>
    </g>
  </svg>
  <svg class="pyramid col-labelled row-4" viewBox="0 0 431 380" role="img" aria-label="MTSS pyramid with tier labels">
    <g clip-path="url(#pyramid-shape)">
      <rect y="-10" width="431" height="137" fill="url(#top-lavender)"/>
      <rect y="127" width="431" height="127" fill="url(#mid-steel)"/>
      <rect y="254" width="431" height="140" fill="url(#base-teal)"/>
      <line class="seam" x1="0" y1="127" x2="431" y2="127"/>
      <line class="seam" x1="0" y1="254" x2="431" y2="254"/>
    </g>
    <text class="label tier-no on-light" x="215.5" y="36">Tier 3</text>
    <text class="label tier-3-name on-light" x="215.5" y="75">Intensive</text>
    <text class="label tier-3-name on-light" x="215.5" y="95">Intervention</text>
    <text class="label tier-no on-dark" x="215.5" y="162">Tier 2</text>
    <text class="label tier-2-name on-dark" x="215.5" y="198">Targeted</text>
    <text class="label tier-2-name on-dark" x="215.5" y="226">Intervention</text>
    <text class="label tier-no on-dark" x="215.5" y="291">Tier 1</text>
    <text class="label tier-1-name on-dark" x="215.5" y="331">Core Instruction</text>
  </svg>

  <!-- Row 5: lavender / cyan / teal -->
  <svg class="pyramid col-plain row-5" viewBox="0 0 431 380" role="img" aria-label="Three-tier MTSS pyramid">
    <g clip-path="url(#pyramid-shape)">
      <rect y="-10" width="431" height="137" fill="url(#top-lavender)"/>
      <rect y="127" width="431" height="127" fill="url(#mid-cyan)"/>
      <rect y="254" width="431" height="140" fill="url(#base-teal)"/>
      <line class="seam" x1="0" y1="127" x2="431" y2="127"/>
      <line class="seam" x1="0" y1="254" x2="431" y2="254"/>
    </g>
  </svg>
  <svg class="pyramid col-labelled row-5" viewBox="0 0 431 380" role="img" aria-label="MTSS pyramid with tier labels">
    <g clip-path="url(#pyramid-shape)">
      <rect y="-10" width="431" height="137" fill="url(#top-lavender)"/>
      <rect y="127" width="431" height="127" fill="url(#mid-cyan)"/>
      <rect y="254" width="431" height="140" fill="url(#base-teal)"/>
      <line class="seam" x1="0" y1="127" x2="431" y2="127"/>
      <line class="seam" x1="0" y1="254" x2="431" y2="254"/>
    </g>
    <text class="label tier-no on-light" x="215.5" y="36">Tier 3</text>
    <text class="label tier-3-name on-light" x="215.5" y="75">Intensive</text>
    <text class="label tier-3-name on-light" x="215.5" y="95">Intervention</text>
    <text class="label tier-no on-light" x="215.5" y="162">Tier 2</text>
    <text class="label tier-2-name on-light" x="215.5" y="198">Targeted</text>
    <text class="label tier-2-name on-light" x="215.5" y="226">Intervention</text>
    <text class="label tier-no on-dark" x="215.5" y="291">Tier 1</text>
    <text class="label tier-1-name on-dark" x="215.5" y="331">Core Instruction</text>
  </svg>

</div>
</body>
</html>
```